Professionelles Webdesign für hochwertiges Coaching Business
Zielgruppe
Es geht um eine Coaching-Firma für Einzelcoaching, Team-Coaching in Firmen und Ausbildungen. Inhalt sind Kommunikation, Stressmanagement und Leistungssteigerung, Persönlichkeitsentwicklung bis hin zum Marketing für Coaches.
Aufgabenstellung
- siehe Briefing im Dateiupload
- Umsetzung via Baukastensystem. Wichtig ist, dass die Features mit dem Baukastensystem umsetzbar sind.
- Es dürfen bitte diese 4 Seiten gestaltet werden:
Startseite
Coaching
Training
Ausbildung
- Obgleich ich Kundenfokus auf der Website bevorzuge, darf sie mich auch etwas widerspiegeln. Für einen Eindruck über mich sind zwei Bilder dem Anhang beigefügt. Diese Bilder sollen NICHT in die Website eingebunden werden.

```html
<!DOCTYPE html>
<html lang="de">
<head>
<meta charset="utf-8">
<title>Halvorsen Coaching – Startseite</title>
<link rel="stylesheet" href="https://fonts.googleapis.com/css2?family=Work+Sans:wght@300;400;600&display=swap">
<style>
  :root {
    --white: #ffffff;
    --ink: #2b2b2b;
    --accent: #a3202c;
    --hero-dark: #2f3a33;
    --hero-mid: #4b5a4f;
    --hero-light: #7d8a80;
    --hero-text: #ffffff;
    --hero-sub: rgba(255,255,255,0.88);
  }
  * { box-sizing: border-box; margin: 0; padding: 0; }
  html, body {
    width: 1200px;
    height: 2602px;
    overflow: hidden;
    background: var(--white);
    font-family: "Work Sans", Arial, sans-serif;
  }
  .site-header {
    height: 300px;
    display: flex;
    align-items: center;
    justify-content: space-between;
    padding: 0 130px 0 88px;
    background: var(--white);
  }
  .brand {
    display: flex;
    align-items: center;
    gap: 22px;
    color: var(--ink);
    font-weight: 600;
    font-size: 44px;
    letter-spacing: 2px;
    text-transform: uppercase;
  }
  .brand-dot {
    width: 34px;
    height: 34px;
    border-radius: 50%;
    background: var(--accent);
  }
  .menu-toggle {
    width: 106px;
    height: 36px;
    display: flex;
    flex-direction: column;
    justify-content: space-between;
  }
  .menu-toggle span {
    display: block;
    height: 2px;
    background: var(--ink);
  }
  .hero {
    position: relative;
    height: 2302px;
    overflow: hidden;
  }
  .hero-photo {
    position: absolute;
    inset: 0;
    background:
      radial-gradient(ellipse at 75% 20%, #3e5a45 0%, transparent 55%),
      radial-gradient(ellipse at 30% 75%, #8795a0 0%, transparent 50%),
      linear-gradient(160deg, var(--hero-dark) 0%, var(--hero-mid) 50%, var(--hero-light) 100%);
  }
  .hero-shade {
    position: absolute;
    inset: 0;
    background: rgba(30, 36, 32, 0.35);
  }
  .hero-content {
    position: absolute;
    left: 73px;
    right: 40px;
    top: 400px;
    color: var(--hero-text);
  }
  .hero-title {
    font-weight: 400;
    font-size: 78px;
    line-height: 110px;
    letter-spacing: -0.5px;
    overflow-wrap: normal;
    word-break: normal;
    hyphens: manual;
    margin-bottom: 110px;
  }
  .hero-lead {
    font-weight: 300;
    font-size: 60px;
    line-height: 108px;
    color: var(--hero-sub);
    padding-right: 30px;
  }
</style>
</head>
<body>
  <header class="site-header">
    <div class="brand"><span class="brand-dot"></span>Halvorsen Coaching</div>
    <div class="menu-toggle" aria-label="Menü"><span></span><span></span></div>
  </header>
  <section class="hero">
    <div class="hero-photo" role="img" aria-label="Foto: Coaching-Gespräch zweier Personen mit Wasserglas vor grünen Zimmerpflanzen"></div>
    <div class="hero-shade"></div>
    <div class="hero-content">
      <h1 class="hero-title">Ich unterstütze Sie in Persönlichkeits&shy;entwicklung und Kompetenzcoaching</h1>
      <p class="hero-lead">Coaching für Privatpersonen und Teams in Firmen – persönlich vor Ort oder ganz bequem von zu Hause.</p>
    </div>
  </section>
</body>
</html>
```